PR & Jobs Workshop

We need a eye catching poster design (standard size) to attract people to register and attend a workshop. These will be posted in cafes, notice boards, grocery stores across the city.
Target Market(s)
Target audience is young people between 20-35 age.
Colors
Designer to choose colors to be used in the design.
Requirements
Must have
- (Main Heading)
- Free Jobs & PR Workshop
- (Body)
- What & Who
- - Where & how will I find jobs?
- - What jobs will lead to PR?
- - When & how can my family join me?
- - How much salary do I need?
- - I have a job, do I qualify for PR?
- - I don't have a job, do I qualify for PR?
- To get answers to all these questions, attend a FREE Jobs & PR Workshop by your Friendly & Frank Licensed Immigration Adviser, Dev Malhotra.
- License No: 304718952
- When & Where
- On Sunday, 30 September 2018
- 12-2 pm @ TBC
- TEXT "REGISTER" to 022 487 3920
- LIMITED SEATS ONLY
- (Add photo along with below text)
- Search for 'Dev Malhotra' on VidStream
- (Add logo along with below text)
- www.qrtworldwide.com
Nice to have
- Classy
Should not have
- Avoid too many colors

```html
<!DOCTYPE html>
<html lang="en">
<head>
<meta charset="utf-8">
<title>Jobs &amp; PR Free Workshop – Poster Versions</title>
<link rel="stylesheet" href="https://fonts.googleapis.com/css2?family=Bebas+Neue&family=Montserrat:wght@400;500;700;800&display=swap">
<style>
  :root {
    --board: #474747;
    --yellow: #fdbb1e;
    --orange: #f7941d;
    --ink: #231f20;
    --white: #ffffff;
    --label: #e6e6e6;
    --mark: #e53935;
  }
  * { margin: 0; padding: 0; box-sizing: border-box; }
  html, body { width: 1200px; height: 770px; overflow: hidden; background: var(--board); }
  .board { position: relative; width: 1200px; height: 770px; }

  .poster {
    position: absolute; top: 22px; width: 512px; height: 723px;
    background: var(--yellow); overflow: hidden;
    font-family: "Montserrat", sans-serif; color: var(--ink);
  }
  .poster--one { left: 54px; }
  .poster--two { left: 627px; }

  .poster__people {
    position: absolute; left: 282px; top: 282px; width: 230px; height: 344px;
    background: radial-gradient(ellipse at 55% 45%, rgba(214,150,20,0.45), rgba(214,150,20,0) 70%);
  }
  .poster__frame { position: absolute; left: 0; top: 0; }

  .headline {
    position: absolute; left: 0; width: 100%; text-align: center;
    font-family: "Bebas Neue", sans-serif; line-height: 1; white-space: nowrap;
  }
  .headline--jobs { top: 22px; font-size: 70px; }
  .headline--free { top: 84px; font-size: 72px; }
  .headline--free .accent { color: var(--white); }
  .headline--day { top: 146px; font-size: 46px; }
  .headline--date { top: 184px; font-size: 46px; }
  .headline--time { top: 222px; font-size: 48px; }
  .headline--venue { top: 260px; font-size: 24px; }
  .headline--street { top: 284px; font-size: 24px; }

  .topics__title {
    position: absolute; left: 30px; top: 320px;
    font-size: 26px; font-weight: 800;
  }
  .topics { position: absolute; left: 0; top: 352px; width: 420px; list-style: none; }
  .topic {
    position: relative; height: 27.6px; line-height: 27.6px;
    padding-left: 46px; font-size: 16px; font-weight: 700; white-space: nowrap;
  }
  .topic::before {
    content: ""; position: absolute; left: 33px; top: 12px;
    width: 5px; height: 5px; border-radius: 50%; background: var(--white);
  }
  .topic--band {
    background: linear-gradient(90deg, rgba(247,148,29,0) 0, var(--orange) 22px, var(--orange) 55%, rgba(247,148,29,0) 100%);
    margin-left: 22px; padding-left: 24px; width: 330px;
  }
  .topic--band::before { left: 11px; }
  .topic .hl { color: var(--white); }

  .intro {
    position: absolute; left: 25px; top: 528px; width: 332px;
    font-size: 12px; line-height: 16.4px; text-align: justify;
  }

  .adviser__photo {
    position: absolute; border: 3px solid var(--white);
    background: linear-gradient(160deg, #d9d4cf, #8a7c70);
  }
  .adviser__photo--mara { left: 400px; top: 427px; width: 92px; height: 115px; }
  .adviser__photo--dev { left: 393px; top: 571px; width: 105px; height: 104px;
    background: linear-gradient(170deg, #e4e4e4 0, #bdbdbd 55%, #2b2b2b 100%); }
  .adviser__name {
    position: absolute; font-size: 10px; font-weight: 800; white-space: nowrap;
  }
  .adviser__name--mara { left: 396px; top: 547px; width: 100px; text-align: center; }

  .footer { position: absolute; left: 0; top: 626px; width: 512px; height: 97px; background: var(--white); }
  .brand {
    position: absolute; left: 22px; top: 641px;
    font-size: 50px; font-weight: 800; letter-spacing: -1px; line-height: 1; color: var(--ink);
  }
  .register {
    position: absolute; left: 189px; top: 610px; width: 150px; height: 31px;
    background: var(--ink); border-radius: 6px; text-align: center;
    font-size: 19px; line-height: 31px; color: var(--white); font-weight: 400;
  }
  .register strong { color: var(--yellow); font-weight: 700; }
  .phone {
    position: absolute; left: 132px; top: 643px; width: 260px; text-align: center;
    font-family: "Bebas Neue", sans-serif; font-size: 51px; line-height: 1;
    color: var(--yellow); white-space: nowrap;
  }
  .website {
    position: absolute; left: 144px; top: 689px; width: 240px; text-align: center;
    font-size: 17px; font-weight: 500; white-space: nowrap;
  }
  .channel { position: absolute; left: 392px; top: 683px; width: 120px; height: 30px; }
  .channel__name { position: absolute; left: 6px; top: 0; font-size: 10px; font-weight: 800; white-space: nowrap; }
  .channel__where { position: absolute; left: 16px; top: 15px; font-size: 10px; font-weight: 500; white-space: nowrap; }
  .channel__search { position: absolute; left: 92px; top: 0; }
  .channel__mark { position: absolute; left: 94px; top: 17px; width: 11px; height: 9px; border-radius: 2px; background: var(--mark); }

  .version-label {
    position: absolute; font-family: "Montserrat", sans-serif; font-size: 16px; color: var(--label); white-space: nowrap;
    transform: rotate(-90deg); transform-origin: left top;
  }
  .version-label--one { left: 578px; top: 745px; }
  .version-label--two { left: 1155px; top: 748px; }
</style>
</head>
<body>
<main class="board">

  <article class="poster poster--one">
    <div class="poster__people" role="img" aria-label="Silhouettes of young professionals"></div>
    <svg class="poster__frame" width="512" height="300" viewBox="0 0 512 300" aria-hidden="true">
      <g fill="none" stroke="#ffffff" stroke-width="1.6">
        <polyline points="134,62 32,62 32,280 74,280"/>
        <polyline points="376,62 482,62 482,280 446,280"/>
      </g>
    </svg>
    <h1 class="headline headline--jobs">JOBS &amp; PR</h1>
    <p class="headline headline--free">FREE <span class="accent">WORKSHOP</span></p>
    <p class="headline headline--day">ON SUNDAY</p>
    <p class="headline headline--date">7TH AND 14TH OCTOBER&nbsp; 2018</p>
    <p class="headline headline--time">5-7 PM</p>
    <p class="headline headline--venue">HARBOURVIEW CENTRE, KAURI COMMUNITY HALL</p>
    <p class="headline headline--street">14 TAMAR PL, AUCKLAND CBD.</p>

    <h2 class="topics__title">What &amp; Who</h2>
    <ul class="topics">
      <li class="topic"><span class="hl">What jobs</span> will lead to PR?</li>
      <li class="topic topic--band"><span class="hl">How much salary do I need?</span></li>
      <li class="topic"><span class="hl">Where &amp; how</span> will I find jobs?</li>
      <li class="topic topic--band"><span class="hl">I have a job,</span> do I qualify for PR?</li>
      <li class="topic"><span class="hl">When &amp; how</span> can my family join me?</li>
      <li class="topic topic--band"><span class="hl">I don't have a job,</span> do I qualify for PR?</li>
    </ul>
    <p class="intro">To get answers to all these questions, attend any of these workshops by your Friendly and Frank Licensed Immigration Advisers, Mara Lindqvist (License No: 200913527) &amp; Dev Malhotra (License No: 304718952).</p>

    <div class="adviser__photo adviser__photo--mara" role="img" aria-label="Portrait photo of Mara Lindqvist"></div>
    <p class="adviser__name adviser__name--mara">MARA LINDQVIST</p>

    <div class="footer"></div>
    <div class="brand">QRT</div>
    <div class="register"><strong>REGISTER</strong> to</div>
    <p class="phone">022 487 3920</p>
    <p class="website">www.qrtworldwide.com</p>
    <div class="adviser__photo adviser__photo--dev" role="img" aria-label="Portrait photo of Dev Malhotra"></div>
    <div class="channel">
      <span class="channel__name">DEV MALHOTRA</span>
      <svg class="channel__search" width="14" height="14" viewBox="0 0 14 14" aria-hidden="true"><circle cx="5.5" cy="5.5" r="4.2" fill="none" stroke="#f7941d" stroke-width="1.6"/><line x1="8.6" y1="8.6" x2="13" y2="13" stroke="#f7941d" stroke-width="1.8"/></svg>
      <span class="channel__where">on VidStream</span>
      <span class="channel__mark"></span>
    </div>
  </article>

  <p class="version-label version-label--one">Version 1</p>

  <article class="poster poster--two">
    <div class="poster__people" role="img" aria-label="Silhouettes of young professionals"></div>
    <svg class="poster__frame" width="512" height="300" viewBox="0 0 512 300" aria-hidden="true">
      <g fill="none" stroke="#ffffff" stroke-width="1.6">
        <polyline points="134,62 32,62 32,280 74,280"/>
        <polyline points="376,62 482,62 482,280 446,280"/>
      </g>
    </svg>
    <h1 class="headline headline--jobs">JOBS &amp; PR</h1>
    <p class="headline headline--free">FREE <span class="accent">WORKSHOP</span></p>
    <p class="headline headline--day">ON SUNDAY</p>
    <p class="headline headline--date">7TH AND 14TH OCTOBER&nbsp; 2018</p>
    <p class="headline headline--time">5-7 PM</p>
    <p class="headline headline--venue">HARBOURVIEW CENTRE, KAURI COMMUNITY HALL</p>
    <p class="headline headline--street">14 TAMAR PL, AUCKLAND CBD.</p>

    <h2 class="topics__title">What &amp; Who</h2>
    <ul class="topics">
      <li class="topic"><span class="hl">What jobs</span> will lead to PR?</li>
      <li class="topic topic--band"><span class="hl">How much salary do I need?</span></li>
      <li class="topic"><span class="hl">Where &amp; how</span> will I find jobs?</li>
      <li class="topic topic--band"><span class="hl">I have a job,</span> do I qualify for PR?</li>
      <li class="topic"><span class="hl">When &amp; how</span> can my family join me?</li>
      <li class="topic topic--band"><span class="hl">I don't have a job,</span> do I qualify for PR?</li>
    </ul>
    <p class="intro">To get answers to all these questions, attend any of these workshops by your Friendly and Frank Licensed Immigration Advisers, Mara Lindqvist (License No: 200913527) &amp; Dev Malhotra (License No: 304718952).</p>

    <div class="footer"></div>
    <div class="brand">QRT</div>
    <div class="register"><strong>REGISTER</strong> to</div>
    <p class="phone">022 487 3920</p>
    <p class="website">www.qrtworldwide.com</p>
    <div class="adviser__photo adviser__photo--dev" role="img" aria-label="Portrait photo of Dev Malhotra"></div>
    <div class="channel">
      <span class="channel__name">DEV MALHOTRA</span>
      <svg class="channel__search" width="14" height="14" viewBox="0 0 14 14" aria-hidden="true"><circle cx="5.5" cy="5.5" r="4.2" fill="none" stroke="#f7941d" stroke-width="1.6"/><line x1="8.6" y1="8.6" x2="13" y2="13" stroke="#f7941d" stroke-width="1.8"/></svg>
      <span class="channel__where">on VidStream</span>
      <span class="channel__mark"></span>
    </div>
  </article>

  <p class="version-label version-label--two">Version 2</p>

</main>
</body>
</html>
```